Dean Hollis Business Card

In addition to my name design (file uploaded), black print on white card stock, e-mail address should be presented as a typical e-mail address, i.e., underlined and in blue ink, the card should include the following information:
Professor of Aviation Technology
Accident Litigation Expert Witness
Master Certificated Flight Instructor

dhollis@vexmail.example
Anchorage, Alaska
(907) 318-5074

```html
<!DOCTYPE html>
<html lang="en">
<head>
<meta charset="utf-8">
<title>Dean Hollis Business Card</title>
<link rel="stylesheet" href="https://fonts.googleapis.com/css2?family=Oswald:wght@700&family=Alegreya:ital@1&family=Archivo:wght@800&display=swap">
<style>
  :root {
    --backdrop: #dcdcdc;
    --card: #ffffff;
    --ink: #111111;
    --navy: #2b2f86;
    --link: #1a4fd6;
    --rule: #1a1a1a;
  }
  html, body {
    margin: 0;
    width: 1200px;
    height: 1000px;
    overflow: hidden;
    background: var(--backdrop);
  }
  .card {
    position: absolute;
    left: 100px;
    top: 214px;
    width: 1000px;
    height: 571px;
    background: var(--card);
    box-shadow: 0 0 0 1px #c8c8c8;
  }
  .card__name {
    position: absolute;
    left: 0;
    right: 0;
    top: 28px;
    margin: 0;
    padding-left: 90px;
    text-align: center;
    font-family: "Oswald", sans-serif;
    font-weight: 700;
    font-size: 78px;
    letter-spacing: 3px;
    line-height: 1;
    color: var(--ink);
  }
  .card__rule {
    position: absolute;
    left: 0;
    top: 0;
  }
  .card__titles {
    position: absolute;
    left: 0;
    right: 0;
    top: 170px;
    margin: 0;
    padding: 0;
    list-style: none;
    text-align: center;
    font-family: "Alegreya", serif;
    font-style: italic;
    font-size: 44px;
    line-height: 56px;
    color: var(--navy);
  }
  .card__contact {
    position: absolute;
    left: 60px;
    right: 60px;
    top: 420px;
    margin: 0;
    display: flex;
    justify-content: space-between;
    font-family: "Archivo", sans-serif;
    font-weight: 800;
    font-size: 27px;
    color: var(--ink);
  }
  .card__email {
    color: var(--link);
    text-decoration: underline;
    text-underline-offset: 4px;
    text-decoration-thickness: 2px;
  }
  .card__sep { color: var(--ink); }
</style>
</head>
<body>
  <article class="card">
    <h1 class="card__name">DEAN HOLLIS</h1>

    <svg class="card__rule" width="1000" height="571" viewBox="0 0 1000 571" aria-hidden="true">
      <line x1="60" y1="140" x2="940" y2="140" stroke="var(--rule)" stroke-width="3"/>
      <line x1="60" y1="390" x2="940" y2="390" stroke="var(--rule)" stroke-width="3"/>
    </svg>
    <svg class="card__rule" width="1000" height="571" viewBox="0 0 1000 571">
      <rect role="img" aria-label="airplane silhouette" x="135" y="128" width="60" height="24" rx="12" fill="var(--rule)"/>
      <rect role="img" aria-label="airplane silhouette" x="810" y="378" width="60" height="24" rx="12" fill="var(--rule)"/>
    </svg>

    <ul class="card__titles">
      <li>Professor of Aviation Technology</li>
      <li>Accident Litigation Expert Witness</li>
      <li>Master Certificated Flight Instructor</li>
    </ul>

    <p class="card__contact">
      <span class="card__city">Anchorage, Alaska</span>
      <span class="card__sep">|</span>
      <span class="card__email">dhollis@vexmail.example</span>
      <span class="card__sep">|</span>
      <span class="card__phone">(907) 318-5074</span>
    </p>
  </article>
</body>
</html>
```